Vertical flyer design to guide people to my shop

We need a vertical flyer design for a tailor shop, Marlow Stitchworks. Our shop is on the 3/F, and we need this flyer/poster to placed on the G/F street level to guide people to take the lifts upstairs. Basically to tell people that, "We are here on 3/F!"

Dimensions ratio: 80 (wide) x200 (tall)

You may use the photos and graphics from the webpages below.
http://www.marlowstitchworks.net/en/marlow-stitchworks-hong-kong-tailors-tailor-shop/

https://www.cloth-q.com/tailor/marlow-stitchworks

```html
<!DOCTYPE html>
<html lang="en">
<head>
<meta charset="utf-8">
<title>Marlow Stitchworks – Our Shop Is On The 3rd Floor</title>
<link rel="stylesheet" href="https://fonts.googleapis.com/css2?family=Tinos:wght@400;700&display=swap">
<style>
  :root {
    --backdrop-light: #6f9593;
    --backdrop-mid: #4f7472;
    --backdrop-dark: #344f4e;
    --panel-shade: rgba(52, 52, 52, 0.82);
    --text-light: #ffffff;
    --card-bg: #ffffff;
    --ink: #111111;
  }
  html, body {
    margin: 0;
    padding: 0;
    width: 1200px;
    height: 3000px;
    overflow: hidden;
  }
  .flyer {
    position: relative;
    width: 1200px;
    height: 3000px;
    overflow: hidden;
    font-family: "Tinos", "Times New Roman", serif;
  }
  .backdrop-photo {
    position: absolute;
    inset: 0;
    background:
      radial-gradient(ellipse 70% 40% at 40% 25%, rgba(150, 185, 180, 0.45), transparent 70%),
      linear-gradient(180deg, var(--backdrop-light) 0%, var(--backdrop-mid) 45%, var(--backdrop-dark) 100%);
  }
  .floor-notice {
    position: absolute;
    left: 192px;
    top: 1048px;
    width: 816px;
    height: 1012px;
    background: var(--panel-shade);
    display: flex;
    flex-direction: column;
    justify-content: center;
    align-items: center;
  }
  .floor-notice__line {
    margin: 0;
    color: var(--text-light);
    font-weight: 700;
    font-size: 136px;
    line-height: 188px;
    letter-spacing: 2px;
    text-align: center;
  }
  .brand-card {
    position: absolute;
    left: 192px;
    top: 2128px;
    width: 816px;
    height: 672px;
    box-sizing: border-box;
    background: var(--card-bg);
    border: 16px solid var(--ink);
    display: flex;
    flex-direction: column;
    align-items: center;
    justify-content: center;
    color: var(--ink);
    text-align: center;
  }
  .brand-card__name {
    margin: 0 0 36px;
    font-weight: 700;
    font-size: 96px;
    line-height: 128px;
    letter-spacing: 2px;
  }
  .brand-card__tagline {
    margin: 0;
    font-weight: 400;
    font-size: 58px;
    line-height: 112px;
    letter-spacing: 3px;
  }
</style>
</head>
<body>
  <main class="flyer">
    <div class="backdrop-photo" role="img" aria-label="Photograph of tailoring tools on a teal cloth: large black tailor's shears, a ball of blue yarn, spools of thread and chalk"></div>

    <section class="floor-notice">
      <p class="floor-notice__line">OUR</p>
      <p class="floor-notice__line">SHOP</p>
      <p class="floor-notice__line">IS ON</p>
      <p class="floor-notice__line">THE 3RD</p>
      <p class="floor-notice__line">FLOOR</p>
    </section>

    <section class="brand-card">
      <h1 class="brand-card__name">MARLOW<br>STITCHWORKS</h1>
      <p class="brand-card__tagline">EXPERT LADIES’<br>&amp; GENT’S TAILORS</p>
    </section>
  </main>
</body>
</html>
```